Cause bitches need love too!

I am creating an ad campaign. It will be a series of featured dogs in our shelter and they will contain a picture of the dog wich should be big enough to see on a yard sign and will change every week. I am placing the signs so that they lead you to the shelter. This is why I am also including the copy that says "you're almost there".

I have 4 tag lines:

1. Find unconditional Love.
2. She'll Love you furever!
3. He'll always listen.
4. Meet your new BFF

You're almost there 318 W Harrowgate Ln
Open 10 - 7/Tues-Sat

The dimensions for the sign are 24" wide and 18" high

Every week we will have a different picture of a different dog (hopefully last week's dog gets adopted). Anyhow, I am printing out yard signs, meaning that instead of printing 160 different signs it would be ideal just to replace the photo. So far the copy that is permanent is: "You're almost there. 318 W. Harrowgate Ln."

I could silhouette the image of the dog as well and super impose it on the sign, that's also a consideration, but ideally if I could have 4 tag lines I could print 40 signs of each and just replace the photo manually each week from my printer that would save costs.
Updates

Not enough designs to chose from and I edited the brief and committed to pay no matter what to increase the amount of designs as per your suggestions.

Target Market(s)

Animal lovers

Industry/Entity Type

Campaign

Font styles to use
Sans Serif

Colors

Designer to choose colors to be used in the design.

Requirements
Must have
• The dimensions for the sign are 24" wide and 18" high
Nice to have
• I want the signs to be hip, they should have a positive feel to them. You can alter the photos if you like. I am even open to new copy if you think something else works better.

```html
<!DOCTYPE html>
<html lang="en">
<head>
<meta charset="utf-8">
<title>Shelter Yard Signs</title>
<link href="https://fonts.googleapis.com/css2?family=Roboto:wght@300;400;900&family=Roboto+Condensed:wght@700&display=swap" rel="stylesheet">
<style>
  :root {
    --page-bg: #c9c9cf;
    --sun: #fdb10c;
    --sun-light: #fec334;
    --sun-deep: #e87d17;
    --brick: #c44b38;
    --brick-light: #d3664f;
    --brick-deep: #8a2b20;
    --dot: #ffffff;
    --ink: #1e1e1e;
    --ink-red: #c20d0d;
    --ink-maroon: #6b1010;
    --paper: #f7f7f7;
  }
  html, body {
    margin: 0;
    width: 1200px;
    height: 1200px;
    overflow: hidden;
    background: var(--page-bg);
  }
  .sign-slot {
    position: absolute;
    left: 238px;
    width: 724px;
    height: 542px;
    overflow: hidden;
  }
  .sign-slot--top { top: 48px; }
  .sign-slot--bottom { top: 616px; }
  .sign {
    position: absolute;
    left: 0; top: 0;
    width: 905px;
    height: 678px;
    transform: scale(0.8);
    transform-origin: top left;
    overflow: hidden;
    font-family: "Roboto", sans-serif;
  }
  .sign__art { position: absolute; inset: 0; }
  .line {
    position: absolute;
    right: 20px;
    margin: 0;
    line-height: 1;
    white-space: nowrap;
    text-align: right;
  }
  .headline { font-weight: 900; letter-spacing: -3px; }
  .tagline-a { font-size: 113px; top: 112px; color: var(--ink); }
  .tagline-b { font-size: 73px; top: 210px; color: var(--ink-red); letter-spacing: -2px; }
  .tagline-c { font-size: 80px; top: 269px; color: var(--ink); letter-spacing: -2px; }
  .tagline-meet { font-size: 125px; top: 94px; right: 30px; color: var(--paper); }
  .tagline-new { font-size: 70px; top: 199px; right: 30px; color: var(--ink-red); letter-spacing: -2px; }
  .tagline-bff { font-size: 160px; top: 263px; right: 38px; color: var(--paper); letter-spacing: -4px; }
  .almost {
    font-family: "Roboto Condensed", sans-serif;
    font-weight: 700;
    font-size: 42px;
    top: 497px;
    letter-spacing: -1px;
  }
  .hours {
    position: absolute;
    left: 528px;
    top: 543px;
    margin: 0;
    line-height: 1;
  }
  .hours__open { font-weight: 300; font-size: 56px; letter-spacing: -1px; }
  .hours__detail {
    position: absolute;
    left: 152px;
    font-family: "Roboto Condensed", sans-serif;
    font-weight: 700;
    font-size: 20px;
    white-space: nowrap;
    color: var(--ink-maroon);
  }
  .hours__days { top: 2px; }
  .hours__time { top: 27px; }
  .address {
    font-size: 40px;
    top: 596px;
    color: var(--ink-maroon);
    letter-spacing: -0.5px;
  }
  .sign--sun .almost, .sign--sun .hours__open { color: var(--ink); }
  .sign--brick .almost, .sign--brick .hours__open { color: var(--paper); }
</style>
</head>
<body>

<div class="sign-slot sign-slot--top">
  <section class="sign sign--sun">
    <svg class="sign__art" viewBox="0 0 905 678" width="905" height="678" aria-hidden="false">
      <rect width="905" height="678" fill="var(--sun)"/>
      <circle cx="705" cy="195" r="262" fill="var(--sun-light)"/>
      <circle cx="95" cy="650" r="190" fill="var(--sun-light)"/>
      <g fill="var(--dot)">
        <circle cx="0" cy="68" r="30"/>
        <circle cx="150" cy="80" r="10"/>
        <circle cx="207" cy="-2" r="32"/>
        <circle cx="639" cy="6" r="18"/>
        <circle cx="908" cy="65" r="45"/>
        <circle cx="898" cy="465" r="17"/>
        <circle cx="67" cy="567" r="18"/>
        <circle cx="290" cy="625" r="18"/>
        <circle cx="454" cy="682" r="45"/>
        <circle cx="168" cy="682" r="18"/>
        <circle cx="898" cy="660" r="18"/>
      </g>
      <path fill="var(--sun-deep)" d="M380 92 C470 96 505 190 507 310 C510 440 485 580 355 590 C250 598 90 530 35 475 C10 450 20 400 70 340 C150 240 280 88 380 92 Z"/>
      <defs>
        <linearGradient id="photo-sun" x1="0" y1="0" x2="0" y2="1">
          <stop offset="0" stop-color="#d6d4d2"/>
          <stop offset="0.5" stop-color="#a8865a"/>
          <stop offset="1" stop-color="#4a3a28"/>
        </linearGradient>
      </defs>
      <path role="img" aria-label="Photo of the featured shelter dog, a tan and black shepherd mix" fill="url(#photo-sun)" d="M300 74 C385 70 440 170 485 285 C530 400 515 540 400 555 C300 568 120 540 50 500 C5 470 10 410 60 330 C120 230 210 78 300 74 Z"/>
    </svg>
    <h2 class="line headline tagline-a">SHE'LL</h2>
    <h2 class="line headline tagline-b">LOVE YOU</h2>
    <h2 class="line headline tagline-c">FUREVER!</h2>
    <p class="line almost">You're almost there</p>
    <p class="hours">
      <span class="hours__open">OPEN</span>
      <span class="hours__detail hours__days">Tuesday to Saturday</span>
      <span class="hours__detail hours__time">Time: 10 AM to 7 PM</span>
    </p>
    <p class="line address">318 W Harrowgate Ln</p>
  </section>
</div>

<div class="sign-slot sign-slot--bottom">
  <section class="sign sign--brick">
    <svg class="sign__art" viewBox="0 0 905 678" width="905" height="678">
      <rect width="905" height="678" fill="var(--brick)"/>
      <circle cx="705" cy="195" r="262" fill="var(--brick-light)"/>
      <circle cx="95" cy="650" r="190" fill="var(--brick-light)"/>
      <g fill="var(--dot)">
        <circle cx="0" cy="68" r="30"/>
        <circle cx="150" cy="80" r="10"/>
        <circle cx="207" cy="-2" r="32"/>
        <circle cx="639" cy="6" r="18"/>
        <circle cx="908" cy="65" r="45"/>
        <circle cx="898" cy="465" r="17"/>
        <circle cx="67" cy="567" r="18"/>
        <circle cx="290" cy="625" r="18"/>
        <circle cx="454" cy="682" r="45"/>
        <circle cx="168" cy="682" r="18"/>
        <circle cx="898" cy="660" r="18"/>
      </g>
      <path fill="var(--brick-deep)" d="M380 92 C470 96 505 190 507 310 C510 440 485 580 355 590 C250 598 90 530 35 475 C10 450 20 400 70 340 C150 240 280 88 380 92 Z"/>
      <defs>
        <linearGradient id="photo-brick" x1="0" y1="0" x2="0" y2="1">
          <stop offset="0" stop-color="#cfcfd0"/>
          <stop offset="0.5" stop-color="#8e8582"/>
          <stop offset="1" stop-color="#c9c4c2"/>
        </linearGradient>
      </defs>
      <path role="img" aria-label="Photo of the featured shelter dog, a grey and white pit bull mix" fill="url(#photo-brick)" d="M300 74 C385 70 440 170 485 285 C530 400 515 540 400 555 C300 568 120 540 50 500 C5 470 10 410 60 330 C120 230 210 78 300 74 Z"/>
    </svg>
    <h2 class="line headline tagline-meet">MEET</h2>
    <h2 class="line headline tagline-new">YOUR NEW</h2>
    <h2 class="line headline tagline-bff">BFF</h2>
    <p class="line almost">You're almost there</p>
    <p class="hours">
      <span class="hours__open">OPEN</span>
      <span class="hours__detail hours__days">Tuesday to Saturday</span>
      <span class="hours__detail hours__time">Time: 10 AM to 7 PM</span>
    </p>
    <p class="line address">318 W Harrowgate Ln</p>
  </section>
</div>

</body>
</html>
```